Brisk Canopy Builders needs a product brochure

We need a new flyer for our Porch Nook Lounge. Here is some of the copy your will need.
"Turn your back yard into the ultimate entertianment venue with the stunning Porch Nook Lounge!"
"Entertain family & friends in your very own back yard!"
"Available with or without solar and comes in a variety of colors"
"The Porch Nook Lounge measures 5' deep by 10' wide and is 9'-6" at it's highest point"
"Constructed with treated 4x4's, primed then painted with Garrick Pellman best exterior paint for years of care free enjoyment. Also, Farley Dunmore Steadfast shingles are dimensional, have a 25 year warranty and are rated for 150 mph winds!"
"TV Mount included. Shelves and TV are sold separately"
There also needs to be a box where we can add the price into later. The price can change from time to time due to material cost fluctuation.

```html
<!DOCTYPE html>
<html lang="en">
<head>
<meta charset="utf-8">
<title>Porch Nook Lounge Flyer</title>
<link href="https://fonts.googleapis.com/css2?family=Montserrat:wght@500;600;700;800&display=swap" rel="stylesheet">
<style>
  :root {
    --stage: #e9e7e4;
    --green: #4f9a35;
    --orange: #f19a1a;
    --ink: #1d1d1d;
    --sky-top: #e4f3fb;
    --sky-bottom: #8fc8ec;
    --mustard: #e2ab2a;
    --photo-dark: #2f3337;
    --photo-wood: #b8793f;
    --tick: #f3a21d;
  }
  * { box-sizing: border-box; margin: 0; padding: 0; }
  html, body { width: 1200px; height: 800px; overflow: hidden; }
  body {
    background: var(--stage);
    font-family: "Montserrat", sans-serif;
    color: var(--ink);
  }
  .flyer {
    position: absolute;
    left: 320px; top: 10px;
    width: 560px; height: 780px;
    overflow: hidden;
    background: linear-gradient(180deg, #f3f3ef 0%, #eef0ea 40%, var(--sky-top) 58%, var(--sky-bottom) 100%);
    box-shadow: 0 6px 24px rgba(0,0,0,.18);
  }
  .hero-photo {
    position: absolute; left: 285px; top: 0; width: 275px; height: 370px;
    background: linear-gradient(160deg, #c9cfa8 0%, #8c8f86 35%, var(--photo-wood) 55%, var(--photo-dark) 72%, #3f8a34 100%);
  }
  .brand {
    position: absolute; left: 30px; top: 226px;
    display: flex; align-items: center; gap: 8px;
  }
  .brand-dot { width: 14px; height: 14px; border-radius: 50%; background: var(--green); }
  .brand-name { font-weight: 800; font-size: 16px; color: var(--orange); }
  .headline {
    position: absolute; left: 30px; top: 262px; width: 245px;
    font-weight: 800; font-size: 15px; line-height: 1.3;
    white-space: nowrap;
  }
  .headline .g { color: var(--green); display: block; }
  .headline .o { color: var(--orange); display: block; }
  .feature-band {
    position: absolute; left: 0; top: 370px; width: 560px; height: 92px;
    background: var(--green);
    padding: 12px 30px;
    display: flex; flex-direction: column; gap: 8px;
  }
  .feature {
    display: flex; gap: 8px; align-items: flex-start;
    color: #fff; font-weight: 700; font-size: 11.5px; line-height: 1.3; width: 285px;
  }
  .feature svg { flex: none; margin-top: 1px; }
  .shelf-photo {
    position: absolute; left: 335px; top: 390px; width: 205px; height: 105px;
    background: linear-gradient(135deg, #24282c, #5a6470 55%, #1c1f22);
  }
  .bar-photo {
    position: absolute; left: 330px; top: 510px; width: 230px; height: 200px;
    background: linear-gradient(170deg, #3c4248 0%, var(--photo-wood) 40%, var(--photo-dark) 70%, var(--mustard) 100%);
  }
  .dims {
    position: absolute; left: 30px; top: 474px; width: 290px;
    font-weight: 800; font-size: 12px; line-height: 1.3;
  }
  .details {
    position: absolute; left: 30px; top: 518px; width: 290px;
    font-weight: 600; font-size: 11px; line-height: 1.38;
  }
  .tv-note {
    position: absolute; left: 30px; top: 620px; width: 290px;
    font-weight: 800; font-size: 12px; line-height: 1.3;
  }
  .footer-band {
    position: absolute; left: 0; top: 700px; width: 560px; height: 80px;
    background: var(--mustard);
  }
  .price-box {
    position: absolute; left: 30px; top: 664px; width: 280px; height: 76px;
    background: #fff; border-radius: 8px; overflow: hidden;
    box-shadow: 0 2px 6px rgba(0,0,0,.12);
  }
  .price-box h2 {
    background: var(--green); color: #fff;
    font-size: 11px; font-weight: 800; text-align: center;
    padding: 5px 0; letter-spacing: .3px;
  }
  .contact {
    position: absolute; left: 30px; top: 748px;
    font-style: normal; font-weight: 700; font-size: 10px; line-height: 1.4;
  }
  .contact-line { display: flex; align-items: center; gap: 5px; }
  .contact-row { display: flex; gap: 16px; }
</style>
</head>
<body>
  <main class="flyer">
    <div class="hero-photo" role="img" aria-label="Photo of the Porch Nook Lounge bar with friends watching TV and a dog on green turf"></div>

    <div class="brand">
      <span class="brand-dot"></span>
      <span class="brand-name">Brisk Canopy Builders</span>
    </div>

    <h1 class="headline">
      <span class="g">Turn your back yard into</span>
      <span class="o">the ultimate entertianment</span>
      <span class="g">venue with the stunning</span>
      <span class="o">Porch Nook Lounge!</span>
    </h1>

    <section class="feature-band">
      <p class="feature">
        <svg width="14" height="14" viewBox="0 0 14 14"><circle cx="7" cy="7" r="7" fill="var(--tick)"/><path d="M3.8 7.2l2.2 2.2 4.2-4.6" stroke="#fff" stroke-width="1.8" fill="none"/></svg>
        <span>Entertain family &amp; friends<br>in your very own back yard!</span>
      </p>
      <p class="feature">
        <svg width="14" height="14" viewBox="0 0 14 14"><circle cx="7" cy="7" r="7" fill="var(--tick)"/><path d="M3.8 7.2l2.2 2.2 4.2-4.6" stroke="#fff" stroke-width="1.8" fill="none"/></svg>
        <span>Available with or without<br>solar and comes in a variety of colors</span>
      </p>
    </section>

    <div class="shelf-photo" role="img" aria-label="Photo of the bar shelf holding bottles and glasses"></div>
    <div class="bar-photo" role="img" aria-label="Photo of the Porch Nook Lounge with guests seated at the bar"></div>

    <p class="dims">The Porch Nook Lounge measures 5' deep by 10' wide and is 9'-6" at it's highest point</p>

    <p class="details">Constructed with treated 4x4's, primed then painted with Garrick Pellman best exterior paint for years of care free enjoyment. Also, Farley Dunmore Steadfast shingles are dimensional, have a 25 year warranty and are rated for 150 mph winds!</p>

    <p class="tv-note">TV Mount included.<br>Shelves and TV are sold separately</p>

    <div class="footer-band"></div>

    <section class="price-box">
      <h2>PRICE LIST</h2>
    </section>

    <address class="contact">
      <div class="contact-line">
        <svg width="10" height="10" viewBox="0 0 10 10"><circle cx="5" cy="5" r="5" fill="var(--ink)"/><path d="M5 2.2a1.8 1.8 0 0 1 1.8 1.8C6.8 5.4 5 7.8 5 7.8S3.2 5.4 3.2 4A1.8 1.8 0 0 1 5 2.2z" fill="var(--mustard)"/></svg>
        2150 Maple Crest Ln, Fairbrook, SC 29000
      </div>
      <div class="contact-row">
        <span class="contact-line">
          <svg width="10" height="10" viewBox="0 0 10 10"><circle cx="5" cy="5" r="5" fill="var(--ink)"/><path d="M3.2 2.6l1 1-.5.8c.4.8.9 1.3 1.7 1.7l.8-.5 1 1-.7.8C5 7.2 2.8 5 2.4 3.3z" fill="var(--mustard)"/></svg>
          555-013-4827
        </span>
        <span class="contact-line">
          <svg width="10" height="10" viewBox="0 0 10 10"><circle cx="5" cy="5" r="5" fill="var(--ink)"/><circle cx="5" cy="5" r="2.8" fill="none" stroke="var(--mustard)" stroke-width=".8"/><path d="M2.2 5h5.6M5 2.2v5.6" stroke="var(--mustard)" stroke-width=".7"/></svg>
          www.briskcanopybuilders.example
        </span>
      </div>
    </address>
  </main>
</body>
</html>
```